Whitmore Business Card Design

The name of the business is Dara Whitmore, CPA LLC
The service that we offer is Accounting, Tax & Consulting Services. I need it to have the following items:
Dara Whitmore, Principal
Phone Number
Email Address
Physical Address

I have attached the company logo, one in black and one in white. Please provide a design in black background and the other in white background. Please include "Accounting, Tax & Consulting Services". I want the business card to be clean and very professional.

```html
<!DOCTYPE html>
<html lang="en">
<head>
<meta charset="utf-8">
<title>Dara Whitmore, CPA LLC — Business Card</title>
<link href="https://fonts.googleapis.com/css2?family=Roboto:wght@400;500&display=swap" rel="stylesheet">
<style>
  :root {
    --ink: #2b2b2b;
    --charcoal: #3a3a3b;
    --brand-red: #9b1c1f;
    --paper: #ffffff;
    --backdrop: #f1f1f1;
  }
  * { box-sizing: border-box; margin: 0; padding: 0; }
  html, body {
    width: 1200px; height: 896px; overflow: hidden;
    background: var(--backdrop);
    font-family: "Roboto", Arial, sans-serif;
    color: var(--ink);
  }
  .card {
    position: absolute; left: 335px;
    width: 529px; height: 303px;
    background: var(--paper);
    border-radius: 29px;
    overflow: hidden;
  }
  .card--front { top: 125px; }
  .card--back { top: 473px; }

  /* Front: brand block */
  .brand-mark {
    position: absolute; background: var(--charcoal);
  }
  .card--front .brand-mark { left: 164px; top: 113px; width: 42px; height: 42px; }
  .brand-name {
    position: absolute; white-space: nowrap;
    font-weight: 500; color: var(--charcoal);
    transform: translateX(-50%);
  }
  .card--front .brand-name { left: 185px; top: 166px; font-size: 13px; }

  .divider {
    position: absolute; left: 282px; top: 80px;
    width: 1.5px; height: 146px; background: var(--brand-red);
  }
  .contact { position: absolute; left: 290px; top: 76px; }
  .contact__name {
    font-size: 23px; font-weight: 500; color: var(--brand-red); line-height: 1.2;
  }
  .contact__title { font-size: 12.5px; margin-top: 1px; }
  .contact__address { font-size: 12.5px; line-height: 20px; margin-top: 16px; }
  .contact__line {
    display: flex; align-items: center; gap: 3px;
    font-size: 12.5px; line-height: 20px;
  }
  .contact__line:first-of-type { margin-top: 10px; }
  .contact__line svg { width: 11px; height: 11px; fill: var(--brand-red); flex: none; }

  /* Back */
  .card--back .brand-mark { left: 218px; top: 71px; width: 94px; height: 94px; }
  .card--back .brand-name { left: 265px; top: 184px; font-size: 27px; }
  .service-band {
    position: absolute; left: 0; right: 0; top: 265px; height: 19px;
    background: var(--brand-red); color: var(--paper);
    font-size: 12px; line-height: 19px; text-align: center;
  }
</style>
</head>
<body>
  <section class="card card--front">
    <div class="brand-mark"></div>
    <div class="brand-name">Dara Whitmore, CPA LLC</div>
    <div class="divider"></div>
    <div class="contact">
      <div class="contact__name">Dara Whitmore</div>
      <div class="contact__title">Principal</div>
      <div class="contact__address">Physical Address<br>Harbor Vale CA 90417</div>
      <div class="contact__line">
        <svg viewBox="0 0 24 24" aria-hidden="true"><path d="M6.6 10.8a15.1 15.1 0 0 0 6.6 6.6l2.2-2.2c.3-.3.7-.4 1-.2 1.1.4 2.3.6 3.6.6.6 0 1 .4 1 1V20c0 .6-.4 1-1 1A17 17 0 0 1 3 4c0-.6.4-1 1-1h3.5c.6 0 1 .4 1 1 0 1.3.2 2.5.6 3.6.1.3 0 .7-.2 1z"/></svg>
        <span>123 456 789</span>
      </div>
      <div class="contact__line">
        <svg viewBox="0 0 24 24" aria-hidden="true"><path d="M2 5h20v2l-10 6L2 7zM2 9l10 6 10-6v10H2z"/></svg>
        <span>info@whitmorecpa.com</span>
      </div>
    </div>
  </section>

  <section class="card card--back">
    <div class="brand-mark"></div>
    <div class="brand-name">Dara Whitmore, CPA LLC</div>
    <div class="service-band">Accounting, Tax &amp; Consulting Services</div>
  </section>
</body>
</html>
```